The Copper Gulls -Quiet Tides & Orchards cd

We need artwork for an album cover of our new music CD. We will need it in the Square CD format as well as a 11 x 17 poster size, Photoshop files with layers included. The title of the album is called quiet tides and orchards. The idea for the imagery would be a rope for a string or something frayed and ashes but also incorporate anatomically correct heart. Another theme for inspiration would be day of the dead artwork. Our imagery is often a little dark but playful and lighthearted.

Also the dirty on clean kind of imagery applies!

Previous Pixelbrook cover art winner image is included in files.

Global- Rock Music Fans

Music Download

6b449b
876aae
b7a5cd
e4daeb

• Must have something frayed and ashes in the image. Dirty to clean contrast.
• Anatomical heart ( Possibly the one provided),
• Purple, Episode I font logo
• Heavy Metal styled art work.

```html
<!DOCTYPE html>
<html lang="en">
<head>
<meta charset="utf-8">
<title>The Copper Gulls – Quiet Tides &amp; Orchards</title>
<link rel="stylesheet" href="https://fonts.googleapis.com/css2?family=Big+Shoulders+Display:wght@600&family=Michroma&display=swap">
<style>
  :root {
    --backdrop: #f2efef;
    --cover-black: #050306;
    --cover-edge: #151215;
    --band-violet: #3d1fc4;
    --heart-deep: #2a1846;
    --heart-mid: #6b449b;
    --heart-light: #b7a5cd;
    --pool-violet: #7a4fd6;
    --pool-deep: #3a1f7a;
    --blade-light: #d4d4d8;
    --blade-mid: #8f8f94;
    --title-grey: #55535a;
  }
  * { margin: 0; padding: 0; box-sizing: border-box; }
  html, body {
    width: 1200px; height: 900px; overflow: hidden;
    background: var(--backdrop);
  }
  .album-cover {
    position: absolute; left: 290px; top: 140px;
    width: 620px; height: 620px;
    background: radial-gradient(ellipse at 50% 40%, #0b080d 0%, var(--cover-black) 60%, var(--cover-edge) 100%);
    overflow: hidden;
  }
  .scissors-art {
    position: absolute; left: 200px; top: 30px; width: 264px; height: 80px;
    background: radial-gradient(ellipse 50% 30% at 50% 50%, var(--blade-light) 0%, var(--blade-mid) 45%, rgba(143,143,148,0) 100%);
    opacity: .8;
  }
  .heart-art {
    position: absolute; left: 210px; top: 90px; width: 190px; height: 430px;
    background: radial-gradient(ellipse 50% 50% at 50% 45%, var(--heart-light) 0%, var(--heart-mid) 35%, var(--heart-deep) 65%, rgba(42,24,70,0) 100%);
  }
  .pool-art {
    position: absolute; left: 80px; top: 525px; width: 440px; height: 70px;
    background: radial-gradient(ellipse 50% 50% at 50% 50%, var(--pool-violet) 0%, var(--pool-deep) 60%, rgba(58,31,122,0) 100%);
  }
  .band-name {
    position: absolute; left: 0; top: 326px;
    font-family: "Big Shoulders Display", sans-serif;
    font-weight: 600; font-size: 66px; line-height: 56px;
    color: var(--band-violet);
    text-transform: uppercase; letter-spacing: 2px;
  }
  .band-name span { display: block; }
  .band-name .line-one { padding-left: 104px; }
  .band-name .line-two { padding-left: 28px; }
  .band-name .line-three { padding-left: 90px; }
  .album-title {
    position: absolute; left: 0; right: 0; top: 552px;
    text-align: center;
    font-family: "Michroma", sans-serif;
    font-weight: 400; font-size: 18px; letter-spacing: 2px;
    color: var(--title-grey);
    text-transform: uppercase;
  }
</style>
</head>
<body>
  <main class="album-cover">
    <div class="scissors-art" role="img" aria-label="Silver scissors poised to cut a thread"></div>
    <div class="heart-art" role="img" aria-label="Violet anatomical heart dripping into a pool"></div>
    <div class="pool-art" role="img" aria-label="Pool of violet liquid beneath the heart"></div>
    <h1 class="band-name">
      <span class="line-one">The</span>
      <span class="line-two">Copper</span>
      <span class="line-three">Gulls</span>
    </h1>
    <h2 class="album-title">quiet tides and orchards</h2>
  </main>
</body>
</html>
```